Back Pain

Need a flyer similar to the attached draft. This is to be handed out to prospective patients. Note that Sketch Hive has already designed the logo. If you need a copy please contact me

```html
<!DOCTYPE html>
<html lang="en">
<head>
<meta charset="utf-8">
<title>Tech Neck Back Pain Relief Clinic Flyer</title>
<link rel="stylesheet" href="https://fonts.googleapis.com/css2?family=Bebas+Neue&family=Roboto+Condensed:wght@700&family=Saira+Semi+Condensed:wght@500&family=Raleway:wght@300;400;700;800&display=swap">
<style>
  :root {
    --sky-light: #f2fbfe;
    --white: #ffffff;
    --violet: #6a32ee;
    --violet-bar: #7a2ff0;
    --lime: #3be12a;
    --lime-soft: #7ddb4a;
    --azure: #3a8fe3;
    --azure-label: #3d83d8;
    --navy: #1b2a44;
    --ink: #111111;
    --alert: #ff0000;
    --figure: #b9bfc4;
  }
  * { margin: 0; padding: 0; box-sizing: border-box; }
  html, body { width: 849px; height: 1200px; overflow: hidden; }
  body { background: var(--sky-light); }
  .flyer { position: relative; width: 849px; height: 1200px; overflow: hidden;
    background: linear-gradient(180deg, #e4f6fc 0%, var(--sky-light) 45%, #eaf8fd 100%); }
  .waves { position: absolute; inset: 0; }
  .abs { position: absolute; white-space: nowrap; }

  .title-main { left: 28px; top: 36px; font: 121px/1 "Bebas Neue", sans-serif; color: var(--white); letter-spacing: -1px; }
  .title-sub { left: 34px; font: 88px/1 "Bebas Neue", sans-serif; color: var(--violet); }
  .title-sub.line1 { top: 152px; }
  .title-sub.line2 { top: 240px; }

  .chart-caption { left: 61px; top: 411px; font: 700 19.5px/22px "Roboto Condensed", sans-serif; color: var(--ink); }
  .head-figure { left: 53px; top: 483px; width: 88px; height: 89px;
    background: linear-gradient(180deg, #1a1a1a 0%, #3a3a3a 100%); }
  .chart { left: 50px; top: 455px; }
  .bar-value { font: 31px "Bebas Neue", sans-serif; fill: var(--white); text-anchor: middle; }
  .tick-label { font: 34px "Bebas Neue", sans-serif; fill: var(--ink); text-anchor: middle; }
  .axis-title { left: 75px; top: 707px; font: 700 17px "Roboto Condensed", sans-serif; color: var(--ink); letter-spacing: .3px; }
  .axis-vertical { font: 700 13px "Roboto Condensed", sans-serif; fill: var(--ink); }

  .person { left: 543px; top: 137px; width: 235px; height: 821px;
    background: linear-gradient(180deg, #a9b0b5 0%, var(--figure) 40%, #9ea6ab 100%);
    opacity: .85; }
  .markers { left: 0; top: 0; }
  .pain-label { font: 500 22px/22px "Saira Semi Condensed", "Arial Narrow", sans-serif; color: var(--azure-label); }

  .pitch { left: 46px; font-family: "Bebas Neue", sans-serif; }
  .pitch.l1 { top: 790px; font-size: 50px; color: var(--azure); }
  .pitch.l2 { top: 841px; font-size: 30px; letter-spacing: 2px; color: var(--lime); }
  .pitch.l3 { top: 872px; font-size: 46px; color: var(--azure); }
  .pitch.l4 { top: 913px; font-size: 46px; color: var(--violet); }
  .lime { color: var(--lime); }
  .navy { color: var(--navy); }
  .azure { color: var(--azure); }

  .divider { left: 53px; top: 980px; width: 742px; height: 1px; background: var(--navy); }

  .footer { left: 0; width: 849px; text-align: center; font-family: "Raleway", sans-serif; }
  .footer.location { top: 1000px; font-size: 33px; font-weight: 300; color: var(--lime-soft); }
  .footer.offer { top: 1042px; font-size: 35px; font-weight: 800; color: var(--azure); letter-spacing: .5px; }
  .footer.prompt { top: 1087px; font-size: 29px; font-weight: 400; color: var(--ink); }
  .footer.url { top: 1123px; font-size: 37px; font-weight: 800; color: var(--ink); }
</style>
</head>
<body>
<main class="flyer">
  <svg class="waves" width="849" height="1200" viewBox="0 0 849 1200" aria-hidden="true">
    <path d="M0 0 H849 V110 C700 40 520 10 360 60 C220 100 90 60 0 40 Z" fill="#9ddbf3" opacity=".7"/>
    <path d="M0 160 C80 60 220 20 400 20 C560 20 700 60 849 150 V0 H0 Z" fill="#bfe8f7" opacity=".6"/>
    <path d="M420 300 C600 200 740 220 849 300 V120 C720 150 560 200 420 300 Z" fill="#d4f0fa" opacity=".8"/>
    <path d="M0 1200 V1060 C200 1160 520 1180 849 1080 V1200 Z" fill="#bfe8f7" opacity=".7"/>
    <path d="M300 1200 C500 1130 700 1130 849 1170 V1200 Z" fill="#6fc6ea" opacity=".7"/>
    <path d="M0 1130 C120 1170 240 1190 330 1200 H0 Z" fill="#8fd4f0" opacity=".6"/>
  </svg>

  <h1 class="abs title-main">TECH NECK</h1>
  <div class="abs title-sub line1">BACK PAIN</div>
  <div class="abs title-sub line2">RELIEF CLINIC</div>

  <p class="abs chart-caption">AS THE HEAD TILTS FORWARD.<br>MORE FORCE IS PLACED<br>ON THE SPINE</p>

  <svg class="abs chart" width="320" height="250" viewBox="50 455 320 250" aria-label="Bar chart of pressure on spine by head tilt">
    <rect x="60" y="628" width="39" height="32" fill="var(--lime)"/>
    <rect x="116" y="575" width="40" height="85" fill="var(--lime)"/>
    <rect x="172" y="530" width="38" height="130" fill="var(--azure)"/>
    <rect x="227" y="502" width="40" height="158" fill="var(--violet-bar)"/>
    <rect x="283" y="465" width="39" height="195" fill="var(--navy)"/>
    <text class="bar-value" x="80" y="656">12</text>
    <text class="bar-value" x="136" y="633">27</text>
    <text class="bar-value" x="191" y="611">40</text>
    <text class="bar-value" x="247" y="588">49</text>
    <text class="bar-value" x="302" y="566">60</text>
    <text class="tick-label" x="85" y="697">0°</text>
    <text class="tick-label" x="138" y="697">15°</text>
    <text class="tick-label" x="196" y="697">30°</text>
    <text class="tick-label" x="252" y="697">45°</text>
    <text class="tick-label" x="306" y="697">60°</text>
    <text class="axis-vertical" transform="translate(347 655) rotate(-90)">PRESSURE ON SPIKE (LBS)</text>
  </svg>
  <div class="abs head-figure" role="img" aria-label="Illustration of a head silhouette in side profile tilting forward, with curved arrows"></div>
  <div class="abs axis-title">DEGREES OF FORWARD HEAD TILT</div>

  <div class="abs person" role="img" aria-label="Grey textured 3D figure of a man standing and looking down at his phone"></div>

  <svg class="abs markers" width="849" height="1200" viewBox="0 0 849 1200" aria-hidden="true">
    <g stroke="var(--navy)" stroke-width="1" fill="none">
      <path d="M476 184 H592 L604 178"/>
      <path d="M822 202 H718 L700 220"/>
      <path d="M436 322 H528 L548 296"/>
      <path d="M436 434 H548 L562 396"/>
      <path d="M480 545 H568 L576 522"/>
    </g>
    <g fill="none" stroke="var(--alert)" stroke-width="1">
      <circle cx="610" cy="173" r="17"/><circle cx="610" cy="173" r="23"/>
      <circle cx="689" cy="229" r="17"/><circle cx="689" cy="229" r="23"/>
      <circle cx="557" cy="286" r="17"/><circle cx="557" cy="286" r="23"/>
      <circle cx="569" cy="386" r="17"/><circle cx="569" cy="386" r="23"/>
      <circle cx="741" cy="448" r="17"/><circle cx="741" cy="448" r="23"/>
      <circle cx="581" cy="513" r="17"/><circle cx="581" cy="513" r="23"/>
    </g>
    <g fill="var(--alert)">
      <circle cx="610" cy="173" r="11"/><circle cx="689" cy="229" r="11"/>
      <circle cx="557" cy="286" r="11"/><circle cx="569" cy="386" r="11"/>
      <circle cx="741" cy="448" r="11"/><circle cx="741" cy="448" r="11"/>
      <circle cx="581" cy="513" r="11"/>
    </g>
  </svg>
  <div class="abs pain-label" style="left:476px;top:160px;">Headache</div>
  <div class="abs pain-label" style="left:721px;top:178px;">Neck Pain</div>
  <div class="abs pain-label" style="left:426px;top:278px;text-align:right;width:96px;">Shoulder<br>Pain</div>
  <div class="abs pain-label" style="left:426px;top:378px;text-align:right;width:108px;">Arm &amp;<br>Hand Pain</div>
  <div class="abs pain-label" style="left:702px;top:478px;">Backpain</div>
  <div class="abs pain-label" style="left:480px;top:518px;">Sciatica</div>

  <div class="abs pitch l1">CHIROPRACTIC CARE <span class="lime">CAN HELP</span></div>
  <div class="abs pitch l2">CORRECT AND PREVENT THESE PROBLEMS</div>
  <div class="abs pitch l3"><span class="lime">BY</span> RESTORING <span class="lime">AND</span> <span class="navy">MAINTAINING</span></div>
  <div class="abs pitch l4">PROPER ALIGNMENT <span class="lime">OF THE</span> <span class="azure">NECK</span></div>

  <div class="abs divider"></div>

  <p class="abs footer location">Now in BAYSIDE at 72 Harbour Rd.</p>
  <p class="abs footer offer">50% OFF INITIAL CONSULTATION</p>
  <p class="abs footer prompt">If you book online at</p>
  <p class="abs footer url">www.alignwell.com.au</p>
</main>
</body>
</html>
```